Blog Design for global news commentary

Need a very simple blog template (see attachment, Frontpage) that includes entries and ability to upload photos/video. Tabs are not needed (See Marlo Bistro Vermeil blog for sort of what I am going for but a lot less cluttered). A section that can access old entries is needed as well as a "contact me" tab. The format should be very simple. An entry and section for comments, new entry, section for comments etc. comments sections should be able to be monitored by me. With the ability for readers to contribute via coinlet. The look and feel should be sophisticated and should target an educated global audience. The blog is all about commenting on global news around the world. For example, a news article could be photographed and then commented on. Type face should be simple, clean and 1930's style. See Brindle Post magazine for looks and feel. If viewers wish to contribute they can make donations via coinlet on the site. Once the template is competed it should be very easy for me to update and work with and handed over to a web hosting service. I own the domain name which I want to use. It would be best to use an existing template eg wordpress. So in simple terms need a wordpress template adapted for this blog idea. Not sure what coded vs. uncoded means. But the overall objective is very simple. Template should be clean, no design elements other than the name of the blog.

Target Market(s)

Educated people from around the world interested in current events

Industry/Entity Type

News

Number of Pages Required

2 page

Other font styles liked:
• Upper East Side

Colors
0255a3
1b1b1b
5c5c5c

Requirements
Must have
• This is a blog so it should have all the standard features including daily updates, photo/video upload, comments that can be monitored by me, coinlet donation link. It should be easy for me to use and handle once completed and delivered to web host. It must have a simple, elegant look and feel. I have chose Serif font style but recommend a 1930's Art Deco - clean, unfussy type face. Type face Upper East Side is what I am looking for
Nice to have
• The look must be simple and no pictures, design elements or logos. Clean and crisp
Should not have
• Any pictures for illustrations as part of the overall design

```html
<!DOCTYPE html>
<html lang="en">
<head>
<meta charset="utf-8">
<title>Vantline — Global News Commentary</title>
<link href="https://fonts.googleapis.com/css2?family=Poiret+One&family=Lato:wght@400;700&display=swap" rel="stylesheet">
<style>
:root{
  --blue:#0255a3;
  --ink:#1b1b1b;
  --grey:#5c5c5c;
  --muted:#9a9a9a;
  --rule:#e4e4e4;
  --tint:#f3f3f3;
  --paper:#ffffff;
  --accent:#f0a30a;
  --page:#fafafa;
}
*{box-sizing:border-box;margin:0;padding:0}
html,body{width:1200px;height:2188px;overflow:hidden}
body{background:var(--page);font-family:'Lato',sans-serif;color:var(--grey);font-size:10px;line-height:1.55;position:relative}
.wrap{width:730px;margin:0 auto;position:relative}
.display{font-family:'Poiret One',sans-serif;color:var(--ink);font-weight:400}

/* header */
.site-header{height:120px;display:flex;align-items:center;justify-content:space-between}
.brand{font-family:'Poiret One',sans-serif;font-size:38px;color:var(--blue);letter-spacing:1px}
.util{display:flex;align-items:center;gap:8px;font-size:9px}
.util a{color:var(--muted);text-decoration:none}
.search{width:64px;height:18px;border:1px solid var(--rule);background:#fff}
.btn-register{color:var(--blue);font-weight:700}
.btn-login{background:var(--accent);color:#fff;padding:3px 8px;font-weight:700}

/* hero */
.hero{position:absolute;top:128px;left:0;width:730px;height:234px;background:linear-gradient(160deg,#9fb9c8 0%,#7e8f6b 55%,#5b7a3c 100%)}
.hero-caption{position:absolute;left:0;bottom:18px;background:rgba(20,20,20,.78);padding:8px 18px}
.hero-caption h1{font-family:'Poiret One',sans-serif;color:#fff;font-size:26px;font-weight:400}

/* feature */
.feature{position:absolute;top:378px;left:0;width:730px;height:202px;display:flex;background:var(--ink)}
.feature-media{width:362px;height:100%;background:linear-gradient(135deg,#3a4a3a 0%,#1f6b2b 45%,#222 100%)}
.feature-body{flex:1;padding:20px 24px;color:#bbb}
.feature-body h2{font-family:'Poiret One',sans-serif;color:#fff;font-size:26px;font-weight:400;line-height:1.2;margin-bottom:12px}

/* grid */
.grid{position:absolute;top:596px;left:0;width:730px;display:flex;gap:12px}
.col{width:235px;display:flex;flex-direction:column;gap:10px}
.card{background:var(--paper);border:1px solid var(--rule);padding:16px 15px;display:flex;flex-direction:column;overflow:hidden}
.card--tint{background:var(--tint)}
.card h3{font-family:'Poiret One',sans-serif;color:var(--ink);font-size:25px;font-weight:400;line-height:1.15;margin-bottom:10px}
.card p{flex:1}
.card-media{margin:-16px -15px 14px;height:120px}
.media-stage{background:linear-gradient(135deg,#3b2a22,#7a4a2c 50%,#1e2233)}
.media-video{background:linear-gradient(135deg,#0d1b2e,#1c4d7a 55%,#0a0f18)}
.meta{display:flex;gap:14px;margin-top:10px;color:var(--muted);font-size:9px;align-items:center}
.meta span{display:flex;align-items:center;gap:4px}
.h-214{height:214px}.h-190{height:190px}.h-400{height:400px}.h-204{height:204px}.h-196{height:196px}.h-404{height:404px}.h-200{height:200px}

.divider{position:absolute;top:1446px;left:0;width:730px;border-top:2px solid var(--ink)}

/* lists */
.section-title{position:absolute;left:0;font-family:'Poiret One',sans-serif;color:var(--blue);font-size:30px}
.row{position:absolute;left:0;width:730px;display:flex;gap:10px}
.row .card{width:175px;height:162px;padding:14px 12px}
.row .card h3{font-size:20px}

/* newsletter */
.newsletter{position:absolute;top:1728px;left:0;width:730px;height:44px;background:var(--ink);display:flex;align-items:center;padding:0 18px;gap:10px}
.newsletter h4{font-family:'Poiret One',sans-serif;color:#fff;font-size:22px;font-weight:400;flex:1}
.field{width:140px;height:22px;background:#fff;color:var(--muted);font-size:9px;padding:4px 8px}
.btn-subscribe{background:var(--blue);color:#fff;font-size:9px;font-weight:700;padding:5px 14px}

/* footer */
.site-footer{position:absolute;top:2070px;left:0;width:1200px;height:118px;background:#111;color:#888;text-align:center;padding-top:26px;font-size:9px}
.footer-nav{display:flex;justify-content:center;gap:16px;margin-bottom:14px}
.social{display:flex;justify-content:center;gap:6px;margin-bottom:12px}
.social i{width:14px;height:14px;border-radius:50%;display:block}
</style>
</head>
<body>
<div class="wrap">
  <header class="site-header">
    <div class="brand">Vantline</div>
    <nav class="util">
      <a>About</a><a>Archive</a><a>Contact</a>
      <div class="search"></div>
      <span class="btn-register">Register</span>
      <span class="btn-login">Login</span>
    </nav>
  </header>

  <section class="hero" role="img" aria-label="Photo of runners in a city race">
    <div class="hero-caption"><h1>Headline text here</h1></div>
  </section>

  <section class="feature">
    <div class="feature-media" role="img" aria-label="Photo of a television crew filming a presenter"></div>
    <div class="feature-body">
      <h2>Aenean volutpat nec augue tincidunt consequat</h2>
      <p>Sed ut perspiciatis unde omnis iste natus error sit voluptatem accusantium doloremque laudantium, totam rem aperiam eaque ipsa quae ab illo inventore veritatis et quasi architecto beatae vitae dicta sunt.</p>
    </div>
  </section>

  <section class="grid">
    <div class="col">
      <article class="card h-214"><h3>Nam sit amet enim eget risus</h3><p>Sed ut perspiciatis unde omnis iste natus error sit voluptatem accusantium doloremque laudantium, totam rem aperiam eaque ipsa quae ab illo.</p><div class="meta"><span>● 24</span><span>▪ 6</span></div></article>
      <article class="card card--tint h-190"><h3>Nam sit amet enim eget risus</h3><p>Sed ut perspiciatis unde omnis iste natus error sit voluptatem accusantium doloremque laudantium, totam rem aperiam.</p><div class="meta"><span>● 18</span><span>▪ 4</span></div></article>
      <article class="card h-400"><div class="card-media media-stage" role="img" aria-label="Photo of a speaker on a conference stage"></div><h3>Nam sit amet enim eget risus</h3><p>Sed ut perspiciatis unde omnis iste natus error sit voluptatem accusantium doloremque laudantium, totam rem aperiam eaque ipsa quae ab illo inventore veritatis et quasi architecto beatae vitae dicta sunt explicabo nemo enim ipsam.</p><div class="meta"><span>● 31</span><span>▪ 9</span></div></article>
    </div>
    <div class="col">
      <article class="card h-204"><h3>Integer nec numeus lorem lorem elit ullamcorper</h3><p>Sed ut perspiciatis unde omnis iste natus error sit voluptatem accusantium doloremque.</p><div class="meta"><span>● 12</span><span>▪ 3</span></div></article>
      <article class="card h-196"><h3>Integer nec numeus lorem lorem elit ullamcorper</h3><p>Sed ut perspiciatis unde omnis iste natus error sit voluptatem accusantium.</p><div class="meta"><span>● 20</span><span>▪ 5</span></div></article>
      <article class="card card--tint h-190"><h3>Integer nec numeus lorem lorem elit ullamcorper</h3><p>Sed ut perspiciatis unde omnis iste natus error sit voluptatem.</p><div class="meta"><span>● 15</span><span>▪ 2</span></div></article>
      <article class="card h-204"><h3>Integer nec numeus lorem lorem elit ullamcorper</h3><p>Sed ut perspiciatis unde omnis iste natus error sit voluptatem accusantium doloremque.</p><div class="meta"><span>● 27</span><span>▪ 8</span></div></article>
    </div>
    <div class="col">
      <article class="card h-404"><div class="card-media media-video" role="img" aria-label="Still frame of a news video"></div><h3>Sed libero felis et dolor eget lorem aliquet</h3><p>Sed ut perspiciatis unde omnis iste natus error sit voluptatem accusantium doloremque laudantium, totam rem aperiam eaque ipsa quae ab illo inventore veritatis et quasi architecto beatae vitae dicta sunt explicabo.</p><div class="meta"><span>● 40</span><span>▪ 11</span></div></article>
      <article class="card card--tint h-200"><h3>Sed libero felis et dolor eget lorem aliquet</h3><p>Sed ut perspiciatis unde omnis iste natus error sit voluptatem accusantium.</p><div class="meta"><span>● 9</span><span>▪ 1</span></div></article>
      <article class="card h-200"><h3>Sed libero felis et dolor eget lorem aliquet</h3><p>Sed ut perspiciatis unde omnis iste natus error sit voluptatem accusantium.</p><div class="meta"><span>● 22</span><span>▪ 7</span></div></article>
    </div>
  </section>

  <div class="divider"></div>

  <h2 class="section-title" style="top:1488px">Recent Post</h2>
  <section class="row" style="top:1548px">
    <article class="card"><h3>Donec molestie nisi et fellis tincidunt</h3><p>Sed ut perspiciatis unde omnis iste natus error sit voluptatem accusantium doloremque.</p></article>
    <article class="card"><h3>Nullam vestibulum purus vel magna</h3><p>Sed ut perspiciatis unde omnis iste natus error sit voluptatem accusantium doloremque.</p></article>
    <article class="card"><h3>Mauris suscipit felis et dictum cursus</h3><p>Sed ut perspiciatis unde omnis iste natus error sit voluptatem accusantium doloremque.</p></article>
    <article class="card"><h3>Praesent elementum nulla sit amet pede</h3><p>Sed ut perspiciatis unde omnis iste natus error sit voluptatem accusantium doloremque.</p></article>
  </section>

  <section class="newsletter">
    <h4>Newsletter Subscribe</h4>
    <div class="field">Name</div>
    <div class="field">Email</div>
    <span class="btn-subscribe">Subscribe</span>
  </section>

  <h2 class="section-title" style="top:1800px">Most Commented</h2>
  <section class="row" style="top:1858px">
    <article class="card"><h3>Donec molestie nisi et fellis tincidunt</h3><p>Sed ut perspiciatis unde omnis iste natus error sit voluptatem accusantium doloremque.</p></article>
    <article class="card"><h3>Nullam vestibulum purus vel magna</h3><p>Sed ut perspiciatis unde omnis iste natus error sit voluptatem accusantium doloremque.</p></article>
    <article class="card"><h3>Mauris suscipit felis et dictum cursus</h3><p>Sed ut perspiciatis unde omnis iste natus error sit voluptatem accusantium doloremque.</p></article>
    <article class="card"><h3>Praesent elementum nulla sit amet pede</h3><p>Sed ut perspiciatis unde omnis iste natus error sit voluptatem accusantium doloremque.</p></article>
  </section>
</div>

<footer class="site-footer">
  <nav class="footer-nav"><span>Home</span><span>World</span><span>Politics</span><span>Technology</span><span>Health</span><span>Business</span><span>Culture</span><span>Archive</span><span>Contact</span></nav>
  <div class="social">
    <i style="background:#2d6fb0"></i><i style="background:#3aa0d8"></i><i style="background:#c8402f"></i><i style="background:#d13a3a"></i><i style="background:#2e8a57"></i><i style="background:#e07a1f"></i><i style="background:#7a4aa0"></i><i style="background:#1f8fb8"></i>
  </div>
  <p>© 2014 Vantline. All rights reserved.</p>
</footer>
</body>
</html>
```